Direct mail campaign for Corvex Filing Services

Hello. We need a few design options for a direct mail campaign in the name of getting new clients. We are a lien processing company, www.corvexfiling.example (the website is terrible and is in the process of redesign, so just pay attention to the content, not the design)

A "preliminary notice" is a legal document that we send on behalf of our customers. We aren't lawyers and this "notice" only becomes a legal document once the contractor isn't paid for his work. It's basically a document telling the owner or a property that you're working on the betterment of their property and expect to be paid for your work.

I plan on printing this document on something other than paper. I want it to stand out when it's in someone's hand. I haven't decided on what material and it shouldn't effect the design options, but just so you know I'm thinking of something very creative and different. Not a typical postcard.

Target Market(s)

Contractors and suppliers in the construction industry

Industry/Entity Type

Construction

Font styles to use
Serif

Requirements
Must have
• Dedicated and friendly customer service
• Simple and user friendly online interface
• No quotas
• No set-up fees

```html
<!DOCTYPE html>
<html lang="en">
<head>
<meta charset="utf-8">
<title>Corvex Filing Services – Direct Mail Postcard</title>
<link rel="stylesheet" href="https://fonts.googleapis.com/css2?family=Josefin+Slab:wght@300&family=Roboto+Condensed:wght@300;400&family=Open+Sans:wght@400;600&display=swap">
<style>
:root{
  --blue:#0aa3e2;
  --blue-deep:#0a7fb8;
  --charcoal:#3a3a3c;
  --ink:#333;
  --paper:#ffffff;
  --ground:#e9e7e4;
  --rule:#c9c9c9;
}
*{box-sizing:border-box;margin:0;padding:0}
html,body{width:1159px;height:1200px;overflow:hidden}
body{background:var(--ground);position:relative;font-family:"Roboto Condensed",sans-serif;color:var(--ink)}
.card{position:absolute;width:862px;height:560px;background:var(--paper);overflow:hidden;box-shadow:0 3px 10px rgba(0,0,0,.25)}
.card--front{left:94px;top:20px}
.card--back{left:202px;top:618px}

/* front */
.hero-photo{position:absolute;left:0;top:0;width:442px;height:560px;
  background:linear-gradient(120deg,#d9dcd6 0%,#c7763c 22%,#7d8a6a 45%,#4a5a7a 70%,#2d3648 100%)}
.service-band{position:absolute;left:0;top:0;width:442px;height:560px}
.brand-header{position:absolute;left:442px;top:0;width:420px;height:116px;
  background:linear-gradient(90deg,var(--blue) 0%,var(--blue-deep) 100%);color:#fff;text-align:center}
.brand-name{font-family:"Josefin Slab",serif;font-weight:300;color:#fff}
.brand-header .brand-name{font-size:66px;letter-spacing:4px;line-height:1;padding-top:30px}
.brand-tag{font-family:"Josefin Slab",serif;font-weight:300;letter-spacing:3px}
.brand-header .brand-tag{font-size:15px;margin-top:-2px;color:#fff}
.header-rule{position:absolute;left:442px;top:116px;width:420px;height:14px;background:var(--charcoal)}
.benefits{position:absolute;left:468px;top:152px;width:380px}
.benefits h2{font-weight:300;font-size:25px;letter-spacing:.3px;margin:0 0 14px 16px;color:#333}
.benefits ul{list-style:none}
.benefits li{position:relative;padding-left:19px;font-weight:300;font-size:18.5px;line-height:25px}
.benefits li::before{content:"";position:absolute;left:2px;top:8px;width:9px;height:9px;background:var(--blue)}
.contact-bar{position:absolute;left:0;bottom:0;width:100%;height:60px}
.contact-bar svg{position:absolute;left:0;top:0}
.phone,.web{position:absolute;font-family:"Open Sans",sans-serif;font-weight:600;white-space:nowrap;line-height:1}
.card--front .phone{left:470px;top:8px;font-size:17px;color:#fff}
.card--front .web{right:24px;top:37px;font-size:16px;color:#fff;font-weight:400}
.phone svg{position:relative;vertical-align:-3px;margin-right:4px}

/* back */
.back-logo{position:absolute;left:0;top:0;width:422px;height:118px;text-align:center}
.back-logo .brand-name{font-size:66px;letter-spacing:4px;line-height:1;padding-top:28px;color:#111}
.back-logo .brand-tag{font-size:15px;color:#111;margin-top:-2px}
.back-rule{position:absolute;left:0;top:118px;width:422px;height:14px;background:var(--charcoal)}
.about{position:absolute;left:0;top:132px;width:422px;height:370px;
  background:linear-gradient(180deg,var(--blue) 0%,var(--blue-deep) 100%);
  padding:6px 18px 0 26px;color:#fff;font-family:"Open Sans",sans-serif;font-size:13.6px;line-height:19.5px;text-align:justify}
.about p+p{margin-top:19px}
.card--back .contact-bar{width:422px}
.card--back .phone{left:30px;top:7px;font-size:17px;color:#333}
.card--back .web{right:22px;top:39px;font-size:16px;color:#fff;font-weight:400}
.mailing{position:absolute;left:478px;top:28px;font-family:"Open Sans",sans-serif;font-size:17px;line-height:24px;color:#555;font-style:normal}
.mailing .name{color:#222}
.stamp-box{position:absolute;left:716px;top:22px;width:126px;height:71px;border:1px solid var(--rule)}
.address-line{position:absolute;left:481px;width:360px;height:1px;background:var(--rule)}
</style>
</head>
<body>

<section class="card card--front">
  <div class="hero-photo" role="img" aria-label="Photo of a smiling construction worker in a yellow hard hat holding plans beside a cement truck"></div>
  <svg class="service-band" width="442" height="560" viewBox="0 0 442 560">
    <polygon points="0,345 230,560 0,560" fill="#3a3a3c" opacity=".88"/>
    <polygon points="0,430 130,560 112,560 0,448" fill="#0aa3e2"/>
    <polygon points="0,330 245,560 230,560 0,345" fill="#3a3a3c"/>
    <text transform="translate(30,406) rotate(42)" font-family="Open Sans, sans-serif" font-size="16" font-weight="600" fill="#fff">DEDICATED and FRIENDLY</text>
    <text transform="translate(24,428) rotate(42)" font-family="Open Sans, sans-serif" font-size="16" font-weight="600" fill="#fff">CUSTOMER SERVICE</text>
  </svg>

  <header class="brand-header">
    <div class="brand-name">CORVEX</div>
    <div class="brand-tag">FILING SERVICES</div>
  </header>
  <div class="header-rule"></div>

  <div class="benefits">
    <h2>OUR CUSTOMERS CAN EXPECT</h2>
    <ul>
      <li>No set-up fees.</li>
      <li>No quotas.</li>
      <li>Easy set-up... Start Today.</li>
      <li>Convenient monthly billing.</li>
      <li>Free information verification -- ALWAYS!</li>
      <li>Straight-forward billing -- No hidden fees</li>
      <li>Professional customer service.</li>
      <li>Personal attention - We care about you!</li>
      <li>We will beat any competitor's rate for notices and liens.</li>
      <li>Satisfaction Guaranteed!</li>
    </ul>
  </div>

  <div class="contact-bar">
    <svg width="862" height="60" viewBox="0 0 862 60">
      <rect x="442" y="8" width="420" height="52" fill="#3a3a3c"/>
      <polygon points="440,-4 658,-4 632,34 440,34" fill="#0aa3e2"/>
    </svg>
    <div class="phone"><svg width="18" height="18" viewBox="0 0 18 18"><circle cx="9" cy="9" r="8" fill="none" stroke="#fff" stroke-width="1.6"/><path d="M6 4.5l1.6 2.4-1 1c.6 1.3 1.5 2.2 2.8 2.8l1-1 2.4 1.6-1 1.6c-3.6-.4-6.2-3-6.6-6.6z" fill="#fff"/></svg>555.010.2468</div>
    <div class="web">www.corvexfiling.example</div>
  </div>
</section>

<section class="card card--back">
  <div class="back-logo">
    <div class="brand-name">CORVEX</div>
    <div class="brand-tag">FILING SERVICES</div>
  </div>
  <div class="back-rule"></div>
  <div class="about">
    <p>We specialize in preparing Arizona 20-Day Preliminary Notices (prelien) &amp; Mechanic's Liens. We prepare and send via certified and certificate of mailing your Preliminary Notices (preliens) for job sites anywhere within the continental United States, as well as perfecting liens and filing them for you at the appropriate County Recorder's Office. We also give Bonding Notice for city, county, and military jobs. We are established here in Fairview, for your convenience.</p>
    <p>We take the time to make it convenient for you. We can recieve requests in any format: online, fax, email, or by phone. Our online request program is state of the art and includes the option to view your completed 20-day Preliminary Notices online.</p>
    <p>We will beat any competitor's rate for notices and liens, and always exceed their level of service.</p>
  </div>
  <div class="contact-bar">
    <svg width="422" height="60" viewBox="0 0 422 60">
      <rect x="0" y="2" width="422" height="58" fill="#3a3a3c"/>
      <polygon points="0,-4 218,-4 192,36 0,36" fill="#ececec"/>
    </svg>
    <div class="phone"><svg width="18" height="18" viewBox="0 0 18 18"><circle cx="9" cy="9" r="8" fill="none" stroke="#333" stroke-width="1.6"/><path d="M6 4.5l1.6 2.4-1 1c.6 1.3 1.5 2.2 2.8 2.8l1-1 2.4 1.6-1 1.6c-3.6-.4-6.2-3-6.6-6.6z" fill="#333"/></svg>555.010.2468</div>
    <div class="web">www.corvexfiling.example</div>
  </div>

  <address class="mailing">
    <div class="name">Corvex Filing Services</div>
    <div>PO Box 10420</div>
    <div>Fairview, Az 85000</div>
  </address>
  <div class="stamp-box"></div>
  <div class="address-line" style="top:236px"></div>
  <div class="address-line" style="top:287px"></div>
  <div class="address-line" style="top:338px"></div>
  <div class="address-line" style="top:390px"></div>
</section>

</body>
</html>
```